W need a Menu Board designed for a" make your own poke bowl" and Sushi Menu. We would like our logo & Colors to be intergraded with the menu . Also will need to be able to adjust the pricing in the future as needed.

```html
<!DOCTYPE html>
<html lang="en">
<head>
<meta charset="utf-8">
<title>Tidewell Specialty Fish Market – Menu Board</title>
<link href="https://fonts.googleapis.com/css2?family=Montserrat:wght@400;500;700;800&display=swap" rel="stylesheet">
<style>
  :root {
    --brand-blue: #1b4ea6;
    --accent-blue: #6ea6de;
    --ink: #1f2430;
    --rule: #9aa0a8;
    --paper: #f6f7f9;
    --paper-shade: #eceef1;
    --stage: #e8ebee;
  }
  * { margin: 0; padding: 0; box-sizing: border-box; }
  html, body { width: 751px; height: 1200px; overflow: hidden; }
  body {
    background: var(--stage);
    font-family: "Montserrat", sans-serif;
    color: var(--ink);
    position: relative;
  }
  .menu-board {
    position: absolute;
    left: 20px; top: 349px;
    width: 711px; height: 502px;
    background: linear-gradient(90deg, var(--paper) 0%, #fbfbfc 40%, var(--paper-shade) 100%);
    box-shadow: 0 6px 18px rgba(0,0,0,.18);
    overflow: hidden;
  }
  .abs { position: absolute; }

  /* brand */
  .brand-name {
    left: 29px; top: 36px;
    font-weight: 800; font-size: 30px; letter-spacing: 1px;
    color: var(--brand-blue); line-height: 1;
  }
  .brand-est {
    left: 29px; top: 26px; width: 153px;
    display: flex; justify-content: space-between;
    font-size: 5px; font-weight: 500; letter-spacing: 1px; color: var(--accent-blue);
  }
  .brand-tagline {
    left: 29px; top: 84px;
    font-weight: 700; font-size: 9px; letter-spacing: 2.4px;
    color: var(--accent-blue);
  }

  /* photo placeholders */
  .photo { position: absolute; }
  .photo-poke-top { left: 210px; top: -18px; width: 110px; height: 105px; border-radius: 50%;
    background: radial-gradient(circle at 45% 45%, #7fb84a 0%, #c9805f 45%, #c4a07a 75%); }
  .photo-salmon { left: 335px; top: 0; width: 135px; height: 100px; border-radius: 8px;
    background: linear-gradient(135deg, #b98a5a 0%, #f0939a 45%, #e46f72 70%, #d9602e 100%); }
  .photo-noodles { left: 486px; top: -40px; width: 108px; height: 90px; border-radius: 50%;
    background: radial-gradient(circle, #d8a043 0%, #c98b39 55%, #5f8a56 100%); }
  .photo-sushi { left: 600px; top: 4px; width: 80px; height: 82px; border-radius: 50%;
    background: radial-gradient(circle, #f1eadf 0%, #d7c5b0 40%, #222 70%); }
  .photo-plates { left: 419px; top: 198px; width: 250px; height: 76px; border-radius: 40px;
    background: linear-gradient(90deg, #7ea6c8 0%, #a9bf6a 30%, #f0f2f4 50%, #e8916a 72%, #f3f4f5 100%); }
  .photo-poke-bottom { left: 566px; top: 358px; width: 170px; height: 170px; border-radius: 50%;
    background: radial-gradient(circle at 45% 45%, #e7d08a 0%, #a88c62 35%, #6e9a3f 60%, #8a3c6c 80%, #e07a2c 100%); }

  /* brush bands */
  .band {
    position: absolute; height: 16px;
    background: var(--brand-blue);
    clip-path: polygon(2% 8%, 96% 0, 100% 40%, 97% 100%, 0 92%, 1% 50%);
    color: #fff; font-weight: 700; font-size: 9.6px; line-height: 16px;
    padding-left: 12px; letter-spacing: .2px; white-space: nowrap;
  }
  .band--center { padding-left: 0; text-align: center; }
  .band--compact { font-size: 8.6px; letter-spacing: 0; padding-left: 6px; }

  /* lists */
  .list { position: absolute; list-style: none; font-size: 7.6px; line-height: 10.8px; }
  .list li { position: relative; padding-left: 9px; display: flex; align-items: flex-start; }
  .list li::before {
    content: ""; position: absolute; left: 0; top: 3.4px;
    width: 4px; height: 4px; border-radius: 50%; background: var(--brand-blue);
  }
  .list .item { white-space: nowrap; }
  .list .item--wrap { white-space: normal; }
  .list .leader { flex: 1; border-bottom: .6px solid var(--rule); height: 7.5px; margin: 0 5px; min-width: 6px; }
  .list .price { white-space: nowrap; }

  .divider { position: absolute; width: 0; border-left: 1px dotted #555; }

  .poke-start { left: 176px; top: 274px; font-weight: 700; font-size: 9.6px; }
  .choice { position: absolute; top: 297px; font-weight: 700; font-size: 9.6px; }
  .choice span { color: var(--accent-blue); }
</style>
</head>
<body>
<main class="menu-board">

  <!-- photography areas -->
  <div class="photo photo-poke-top" role="img" aria-label="Photo of a poke bowl with salmon, edamame and radish, chopsticks resting on it"></div>
  <div class="photo photo-salmon" role="img" aria-label="Photo of raw salmon fillets on a wooden board with lemon and cherry tomatoes"></div>
  <div class="photo photo-noodles" role="img" aria-label="Photo of a bowl of stir-fried noodles with chopsticks"></div>
  <div class="photo photo-sushi" role="img" aria-label="Photo of sushi rolls on a dark plate with soy sauce"></div>
  <div class="photo photo-plates" role="img" aria-label="Photo of two plates: pasta with egg and grilled salmon with salad"></div>
  <div class="photo photo-poke-bottom" role="img" aria-label="Photo of a colourful bowl with grains, mushrooms, greens and vegetables"></div>

  <!-- brand -->
  <div class="abs brand-est"><span>EST.</span><span>2021</span></div>
  <div class="abs brand-name">TIDEWELL</div>
  <div class="abs brand-tagline">SPECIALTY FISH MARKET</div>

  <!-- sushi rolls -->
  <div class="band" style="left:28px; top:104px; width:136px;">SUSHI ROLLS:</div>
  <div class="band band--center" style="left:561px; top:104px; width:142px;">NEGRI:</div>

  <ul class="list" style="left:39px; top:128px; width:126px;">
    <li><span class="item">Tuna Tartar</span><span class="leader"></span><span class="price">$24.99</span></li>
    <li><span class="item">Salmon</span><span class="leader"></span><span class="price">$22.99</span></li>
    <li><span class="item">Tartar</span><span class="leader"></span><span class="price">$16.99</span></li>
    <li><span class="item">Tuna Tower</span><span class="leader"></span><span class="price">$16.99</span></li>
    <li><span class="item">Salmon</span><span class="leader"></span><span class="price">$18.99</span></li>
  </ul>
  <div class="divider" style="left:183px; top:131px; height:52px;"></div>

  <ul class="list" style="left:203px; top:128px; width:126px;">
    <li><span class="item">Tuna Tataki</span><span class="leader"></span><span class="price">$9.99</span></li>
    <li><span class="item">California Roll</span><span class="leader"></span><span class="price">$7.99</span></li>
    <li><span class="item">Avocado Roll</span><span class="leader"></span><span class="price">$9.99</span></li>
    <li><span class="item">Tuna Roll (Small)</span><span class="leader"></span><span class="price">$9.99</span></li>
    <li><span class="item">Salmon Roll</span><span class="leader"></span><span class="price">$9.99</span></li>
  </ul>
  <div class="divider" style="left:348px; top:131px; height:52px;"></div>

  <ul class="list" style="left:367px; top:128px; width:200px;">
    <li><span class="item">Cucumber Roll</span><span class="leader"></span><span class="price">$7.99</span></li>
    <li><span class="item">Veggie Roll</span><span class="leader"></span><span class="price">$9.99</span></li>
    <li><span class="item">Salmon Avocado Roll</span><span class="leader"></span><span class="price">$9.99</span></li>
    <li><span class="item">Salmon Avocado w/ Salmon on Top</span><span class="leader"></span><span class="price">$14.99</span></li>
    <li><span class="item">Salmon Avocado w/ Tuna on Top</span><span class="leader"></span><span class="price">$14.99</span></li>
  </ul>
  <div class="divider" style="left:578px; top:131px; height:52px;"></div>

  <ul class="list" style="left:602px; top:128px; width:80px;">
    <li><span class="item">Salmon</span></li>
    <li><span class="item">Ahi</span></li>
    <li><span class="item">Wahoo</span></li>
    <li><span class="item">Hamachi</span></li>
    <li><span class="item">Toro</span></li>
  </ul>

  <ul class="list" style="left:39px; top:189px; width:345px;">
    <li><span class="item">Tuna Avocado w/ Tuna on Top</span><span class="leader"></span><span class="price">$14.99</span></li>
    <li><span class="item">Tuna Avocado w/ Salmon on Top</span><span class="leader"></span><span class="price">$14.99</span></li>
    <li><span class="item">Spicy Tuna Roll</span><span class="leader"></span><span class="price">$9.99</span></li>
    <li><span class="item item--wrap" style="width:270px;">Harbor Roll (Inside Out w/ Kani, Cucumber, Avocado, &amp; Tempura Flakes Topped w/ Salmon &amp; Dressed with Eel Sauce)</span><span class="leader"></span><span class="price">$14.99</span></li>
    <li><span class="item item--wrap" style="width:290px;">Lantern Roll (Inside Out w/ Kani, Cucumber &amp; Cilantro Topped w/ Hamachi, Jalapeno &amp; Dressed w/ Cilantro Truffle Sauce)</span><span class="leader"></span><span class="price">$15..99</span></li>
  </ul>

  <!-- poke bowls -->
  <div class="band" style="left:28px; top:275px; width:133px;">POKE BOWLS:</div>
  <div class="abs poke-start">STARTING PRICE $15.99</div>

  <div class="choice" style="left:39px;">CHOICE 1 <span>BASE:</span></div>
  <div class="choice" style="left:192px;">CHOICE 1 <span>PROTEIN:</span></div>
  <div class="choice" style="left:351px;">CHOICE 4 <span>TOPPINGS:</span></div>
  <div class="choice" style="left:557px;">CHOICE 1 <span>CRUNCH:</span></div>

  <ul class="list" style="left:39px; top:317px;">
    <li>White Rice</li><li>Brown Rice</li><li>Quinoa</li><li>Zucchini</li><li>Noodles</li><li>Lettuce</li>
  </ul>
  <div class="divider" style="left:148px; top:313px; height:67px;"></div>

  <ul class="list" style="left:194px; top:317px;">
    <li>Tuna Poke</li><li>Salmon Poke</li><li>Spicy Tuna</li><li>Spicy Salmon</li><li>Kani</li><li>Wahoo</li>
  </ul>
  <div class="divider" style="left:314px; top:313px; height:67px;"></div>

  <ul class="list" style="left:351px; top:317px;">
    <li>Asian Slaw</li><li>Edamame</li><li>Red Onion</li><li>Red Cabbage</li><li>Jalapeno</li><li>Scallions</li><li>Carrot</li>
  </ul>
  <ul class="list" style="left:436px; top:317px;">
    <li>Radish</li><li>Cucumber</li><li>Tomato</li><li>Sprout</li><li>Cilantro</li><li>Pickled Ginger</li>
  </ul>
  <div class="divider" style="left:527px; top:313px; height:67px;"></div>

  <ul class="list" style="left:557px; top:317px;">
    <li>Tempura Flakes</li><li>Toasted Shredded Nori</li><li>Toasted Sesame</li>
  </ul>

  <!-- extras -->
  <div class="band" style="left:28px; top:400px; width:139px;">PREMIUM TOPPINGS:</div>
  <div class="band band--compact" style="left:188px; top:400px; width:172px;">ADDITIONAL PROTEIN SCOOP:</div>
  <div class="band band--center" style="left:370px; top:399px; width:134px;">SAUCES:</div>

  <ul class="list" style="left:39px; top:423px; width:126px;">
    <li><span class="item">Avocado</span><span class="leader"></span><span class="price">$2.00</span></li>
    <li><span class="item">Kani Salad</span><span class="leader"></span><span class="price">$1.00</span></li>
    <li><span class="item">Wakame</span><span class="leader"></span><span class="price">$1.00</span></li>
    <li><span class="item">Mango</span><span class="leader"></span><span class="price">$1.00</span></li>
    <li><span class="item">Pineapple</span><span class="leader"></span><span class="price">$1.00</span></li>
  </ul>

  <ul class="list" style="left:201px; top:423px; width:112px;">
    <li><span class="item">Tuna Poke</span><span class="leader"></span><span class="price">$2.00</span></li>
    <li><span class="item">Salmon Poke</span><span class="leader"></span><span class="price">$1.00</span></li>
    <li><span class="item">Spicy Tuna</span><span class="leader"></span><span class="price">$1.00</span></li>
    <li><span class="item">Spicy Salmon</span><span class="leader"></span><span class="price">$1.00</span></li>
    <li><span class="item">Kani</span><span class="leader"></span><span class="price">$1.00</span></li>
  </ul>
  <div class="divider" style="left:330px; top:427px; height:53px;"></div>

  <ul class="list" style="left:353px; top:424px;">
    <li>Spicy Mayo</li><li>Sweet Chili</li><li>Sriracha</li>
  </ul>
  <ul class="list" style="left:416px; top:424px;">
    <li>Ponzu</li><li>Eel Sauce</li><li>Cilantro Garlic</li>
  </ul>
  <ul class="list" style="left:487px; top:424px;">
    <li>Basil Aioli</li><li>Sesame Ginger</li><li>Carrot Honey</li>
  </ul>

</main>
</body>
</html>
```